Flyer to promote an IT Innovation Fest

BRN Grindstone Gala 2018

We are looking to implement a new Innovation program that uses the Marlow LaunchCrate concept. Team Members will receive a red box that contains a set of 20 flash cards that help them to bring an innovative idea to life (based on a business problem or friction point).
We are looking to create a cover page for our 'Red Box' via way of a 1 page flyer.
We want to call it the 'BRN Grindstone Gala 2018'. We would like the 1 page flyer to look super cool and also have some kind of cool cartoon imagery to bring it to life.
We also want to incorporate our logo into the page somewhere as well.

Ideally, we'd also like to get a logo called 'Grindstone Gala' that we could use on some of our collateral as well. I thought it might be best to create the 1 pager flyer first, then we could look to pull a Grindstone Gala logo off that. Please let me know though whether it would be easier to create the logo first, then create the flyer).

Skyward Ridge Systems are a support business to Skyward Ridge Journeys Group which is the largest travel retailer in Australia. Our IT area has around 150 permanent team members. We have a fun culture and can push the boundaries with our imagery as the flyer will be for internal distribution only.

I have attached the Marlow Flash cards that this 1 pager will be the cover page for.

Target Market(s)

Members of the Skyward Ridge Systems team (internal marketing)

Industry/Entity Type

It Company

Requirements
Must have
• Our BRN Logo
• A super cool, innovative, funky look (with some kind of cartoon imagery)
• We need to be able to edit the flyer to add some text
Nice to have
• Stay within the colour theme of the 'Start Here' page on the Marlow attachment

```html
<!DOCTYPE html>
<html lang="en">
<head>
<meta charset="utf-8">
<title>BRN Grindstone Gala 2018 — Flyer</title>
<link rel="stylesheet" href="https://fonts.googleapis.com/css2?family=Montserrat:wght@100;400;700;800;900&family=Oswald:wght@700&display=swap">
<style>
  :root {
    --stage: #3b3b3b;
    --red-deep: #6c0e21;
    --red-mid: #88142a;
    --red-bright: #a8192f;
    --accent-red: #d8232f;
    --white: #ffffff;
    --ink: #1c1c1c;
    --year-ink: #2e2e2e;
    --bulb-tone: #ececec;
    --bulb-shadow: #8d8d85;
  }
  * { box-sizing: border-box; margin: 0; padding: 0; }
  html, body {
    width: 1200px; height: 1200px; overflow: hidden;
    background: var(--stage);
  }
  .flyer {
    position: absolute; left: 202px; top: 40px;
    width: 795px; height: 1120px;
    background: var(--white);
    font-family: 'Montserrat', sans-serif;
  }
  .hero {
    position: absolute; left: 0; top: 0; width: 795px; height: 917px;
    background:
      radial-gradient(ellipse at 80% 45%, rgba(200,30,50,0.45), transparent 55%),
      radial-gradient(ellipse at 15% 75%, rgba(180,25,45,0.35), transparent 50%),
      linear-gradient(160deg, var(--red-mid) 0%, var(--red-deep) 45%, var(--red-bright) 75%, var(--red-deep) 100%);
    overflow: hidden;
  }
  .hero-frame {
    position: absolute; left: 18px; top: 14px; right: 18px; bottom: -2px;
    border: 1px solid rgba(255,255,255,0.75);
    border-bottom: none;
  }
  .mascot-art {
    position: absolute; left: 32px; top: 159px; width: 310px; height: 642px;
    border-radius: 40px;
    background: radial-gradient(ellipse at 50% 45%, var(--bulb-tone) 0%, rgba(236,236,236,0.55) 40%, rgba(141,141,133,0.25) 70%, transparent 85%);
  }
  .title {
    position: absolute; left: 362px; top: 0; width: 395px;
    color: var(--white);
  }
  .title span { position: absolute; left: 0; white-space: nowrap; }
  .title-code {
    top: 180px; left: -4px;
    font-weight: 900; font-size: 160px; line-height: 1; letter-spacing: -3px;
  }
  .title-main {
    top: 345px;
    font-family: 'Oswald', sans-serif; font-weight: 700;
    font-size: 104px; line-height: 1; letter-spacing: -2px;
    transform: scaleX(0.76); transform-origin: left top;
  }
  .title-sub {
    top: 456px;
    font-weight: 100; font-size: 134px; line-height: 1; letter-spacing: 2px;
  }
  .year-box {
    position: absolute; left: 362px; top: 627px; width: 379px; height: 142px;
    background: var(--white);
    display: flex; align-items: center; justify-content: center;
  }
  .year {
    font-weight: 900; font-size: 130px; line-height: 1; letter-spacing: -5px;
    color: var(--year-ink);
  }
  .footer-band {
    position: absolute; left: 0; top: 917px; width: 795px; height: 174px;
    background: var(--white);
  }
  .brand {
    position: absolute; left: 58px; top: 38px;
    display: flex; align-items: center; gap: 12px;
  }
  .brand-dot {
    width: 44px; height: 44px; border-radius: 50%;
    border: 3px solid var(--ink);
  }
  .brand-name {
    font-weight: 700; font-size: 19px; line-height: 1.15;
    color: var(--accent-red); text-transform: uppercase;
  }
  .contact {
    position: absolute; right: 56px; top: 52px; text-align: right;
  }
  .contact-cta {
    font-weight: 400; font-size: 30px; line-height: 1; color: var(--accent-red);
  }
  .contact-phone {
    margin-top: 10px;
    font-weight: 800; font-size: 50px; line-height: 1; letter-spacing: -1px;
    color: var(--ink);
  }
  .base-strip {
    position: absolute; left: 0; bottom: 0; width: 795px; height: 29px;
    background: #111111;
  }
</style>
</head>
<body>
  <main class="flyer">
    <section class="hero">
      <div class="hero-frame"></div>
      <div class="mascot-art" role="img" aria-label="Cartoon illustration of two office mascots in white shirts and red ties riding a large white light bulb"></div>
      <h1 class="title">
        <span class="title-code">BRN</span>
        <span class="title-main">GRINDSTONE</span>
        <span class="title-sub">GALA</span>
      </h1>
      <div class="year-box"><span class="year">2018</span></div>
    </section>
    <footer class="footer-band">
      <div class="brand">
        <span class="brand-dot"></span>
        <span class="brand-name">Skyward Ridge<br>Systems</span>
      </div>
      <div class="contact">
        <p class="contact-cta">Call Us Now</p>
        <p class="contact-phone">61 7 5550 1234</p>
      </div>
    </footer>
    <div class="base-strip"></div>
  </main>
</body>
</html>
```